Bref créative
Retro design logo for building Materials company
R.K. Morrow Company
Professional
Peter K. Morrow IV
LEED AP BD+C
342 Ferngate Lane, Suite B
Hot Springs, AR 72814
pmorrow@buildwiseterra.com
This is my logo AI file.

```html
<!DOCTYPE html>
<html lang="en">
<head>
<meta charset="utf-8">
<title>R.K. Morrow Company — Stationery</title>
<link rel="stylesheet" href="https://fonts.googleapis.com/css2?family=Libre+Baskerville&family=Lato:wght@400;700&display=swap">
<style>
  :root{
    --stage:#4a3a30;
    --paper:#ffffff;
    --ink:#3a3a3c;
    --ink-soft:#6b6b6e;
    --ghost:#ececec;
    --line:#d6d6d6;
    --swoosh:#2f2f31;
    --swoosh-light:#9a9a9d;
  }
  *{box-sizing:border-box;margin:0;padding:0}
  html,body{width:1200px;height:466px;overflow:hidden;background:var(--stage)}
  .canvas{position:relative;width:1200px;height:466px;font-family:"Lato",sans-serif;color:var(--ink)}
  .sheet{position:absolute;background:var(--paper);box-shadow:0 2px 6px rgba(0,0,0,.35);overflow:hidden}

  .brand{display:flex;align-items:center;gap:5px;font-family:"Libre Baskerville",serif;color:var(--ink);white-space:nowrap}
  .brand-dot{border-radius:50%;background:var(--ink);flex:none}
  .contact{font-size:4.5px;line-height:1.55;color:var(--ink-soft);letter-spacing:.1px}
  .swoosh{position:absolute;left:0;bottom:0;width:100%}

  /* business cards */
  .card-front{left:12px;top:205px;width:136px;height:74px}
  .card-front .brand{position:absolute;left:9px;top:10px;font-size:7px}
  .card-front .brand-dot{width:12px;height:12px}
  .card-front .person{position:absolute;left:9px;top:34px;font-size:5px;font-weight:700;color:var(--ink)}
  .card-front .person span{display:block;font-weight:400;color:var(--ink-soft);font-size:4px}
  .card-front .contact{position:absolute;right:8px;top:34px;text-align:right;font-size:3.8px}
  .card-back{left:12px;top:306px;width:136px;height:76px;background:var(--ink)}
  .card-back .brand{position:absolute;left:50%;top:50%;transform:translate(-50%,-50%);color:var(--paper);font-size:7px}
  .card-back .brand-dot{width:14px;height:14px;background:var(--paper)}

  /* letterheads */
  .letterhead{top:53px;width:268px;height:367px}
  .letterhead-one{left:180px}
  .letterhead-two{left:474px}
  .letterhead-one .brand{position:absolute;left:18px;top:20px;font-size:9px}
  .letterhead-one .brand-dot{width:16px;height:16px}
  .letterhead-one .contact{position:absolute;left:142px;top:20px}
  .watermark{position:absolute;left:50%;top:118px;transform:translateX(-50%);display:flex;flex-direction:column;align-items:center;gap:10px}
  .watermark .brand-dot{width:96px;height:96px;background:var(--ghost)}
  .watermark .brand-name{font-family:"Libre Baskerville",serif;font-size:13px;color:var(--ghost)}
  .letterhead-two .contact{position:absolute;left:0;right:0;bottom:18px;text-align:center;color:var(--paper);z-index:1}

  /* envelopes */
  .envelope{left:775px;width:400px;height:98px}
  .env-flap{position:absolute;left:0;top:0;width:100%;height:100%}
  .env-dark{top:53px;background:var(--ink)}
  .env-split{top:162px}
  .env-white{top:270px;height:80px}
  .env-seal{position:absolute;left:50%;transform:translateX(-50%);border-radius:50%}
  .env-dark .env-seal{top:36px;width:24px;height:24px;background:var(--paper)}
  .env-split .env-seal{top:36px;width:24px;height:24px;background:var(--paper)}
  .env-white .env-seal{top:30px;width:22px;height:22px;background:var(--ink)}
  .env-front{left:770px;top:322px;width:398px;height:98px}
  .env-front .brand{position:absolute;left:14px;top:12px;font-size:8px}
  .env-front .brand-dot{width:14px;height:14px}
  .env-front .contact{position:absolute;left:14px;top:30px;font-size:4px}
</style>
</head>
<body>
<main class="canvas">

  <section class="sheet card-front" aria-label="Business card front">
    <div class="brand"><span class="brand-dot"></span>R.K. MORROW Co.</div>
    <p class="person">Peter K. Morrow IV<span>LEED AP BD+C</span></p>
    <p class="contact">342 Ferngate Lane, Suite B<br>Hot Springs, AR 72814<br>pmorrow@buildwiseterra.com</p>
    <svg class="swoosh" viewBox="0 0 136 20" height="20" preserveAspectRatio="none">
      <path d="M0 14 C40 4 90 22 136 8 L136 20 L0 20 Z" fill="var(--swoosh)"/>
      <path d="M0 11 C40 1 90 18 136 5" stroke="var(--swoosh-light)" stroke-width=".8" fill="none"/>
    </svg>
  </section>

  <section class="sheet card-back" aria-label="Business card back">
    <div class="brand"><span class="brand-dot"></span>R.K. MORROW Co.</div>
  </section>

  <section class="sheet letterhead letterhead-one" aria-label="Letterhead option one">
    <div class="brand"><span class="brand-dot"></span>R.K. MORROW Co.</div>
    <p class="contact">342 Ferngate Lane, Suite B<br>Hot Springs, AR 72814<br>pmorrow@buildwiseterra.com</p>
    <svg class="swoosh" viewBox="0 0 268 40" height="40" preserveAspectRatio="none">
      <path d="M0 30 C70 8 170 40 268 14 L268 40 L0 40 Z" fill="var(--swoosh)"/>
      <path d="M0 25 C70 3 170 33 268 9" stroke="var(--swoosh-light)" stroke-width="1" fill="none"/>
      <path d="M0 21 C80 2 170 28 268 4" stroke="var(--line)" stroke-width=".8" fill="none"/>
    </svg>
  </section>

  <section class="sheet letterhead letterhead-two" aria-label="Letterhead option two">
    <div class="watermark"><span class="brand-dot"></span><span class="brand-name">R.K. MORROW Co.</span></div>
    <p class="contact">342 Ferngate Lane, Suite B &nbsp;·&nbsp; Hot Springs, AR 72814 &nbsp;·&nbsp; pmorrow@buildwiseterra.com</p>
    <svg class="swoosh" viewBox="0 0 268 44" height="44" preserveAspectRatio="none">
      <path d="M0 18 C80 34 180 2 268 20 L268 44 L0 44 Z" fill="var(--swoosh)"/>
      <path d="M0 13 C80 29 180 -3 268 15" stroke="var(--swoosh-light)" stroke-width="1" fill="none"/>
      <path d="M0 9 C80 25 180 -6 268 11" stroke="var(--line)" stroke-width=".8" fill="none"/>
    </svg>
  </section>

  <section class="sheet envelope env-dark" aria-label="Envelope back, dark">
    <svg class="env-flap" viewBox="0 0 400 98" preserveAspectRatio="none">
      <path d="M0 0 L200 50 L400 0" stroke="#55555a" stroke-width="1.2" fill="none"/>
      <path d="M0 98 L150 44 M400 98 L250 44" stroke="#4a4a4e" stroke-width="1" fill="none"/>
    </svg>
    <span class="env-seal"></span>
  </section>

  <section class="sheet envelope env-split" aria-label="Envelope back, dark flap">
    <svg class="env-flap" viewBox="0 0 400 98" preserveAspectRatio="none">
      <path d="M0 0 L400 0 L400 20 L200 64 L0 20 Z" fill="var(--ink)"/>
      <path d="M0 98 L150 50 M400 98 L250 50" stroke="var(--line)" stroke-width="1" fill="none"/>
    </svg>
    <span class="env-seal"></span>
  </section>

  <section class="sheet envelope env-white" aria-label="Envelope back, white">
    <svg class="env-flap" viewBox="0 0 400 80" preserveAspectRatio="none">
      <path d="M0 0 L400 0 L400 12 L200 56 L0 12 Z" fill="#f4f4f4" stroke="var(--line)" stroke-width="1"/>
    </svg>
    <span class="env-seal"></span>
  </section>

  <section class="sheet env-front" aria-label="Envelope front">
    <div class="brand"><span class="brand-dot"></span>R.K. MORROW Co.</div>
    <p class="contact">342 Ferngate Lane, Suite B<br>Hot Springs, AR 72814</p>
    <svg class="swoosh" viewBox="0 0 398 26" height="26" preserveAspectRatio="none">
      <path d="M0 18 C110 4 260 26 398 8 L398 26 L0 26 Z" fill="var(--swoosh)"/>
      <path d="M0 14 C110 0 260 21 398 4" stroke="var(--swoosh-light)" stroke-width="1" fill="none"/>
    </svg>
  </section>

</main>
</body>
</html>
```